Public Adjuster mailing campaign

We are public insurance adjusters. When people (the insured) are not being paid fairly on their insurance claim, we help them get paid all they are owed according to their coverage.We would like a post card mailer to send to homes that have been damaged by a recent tornado. I would like to say something like...Storm Damage?Is your insurance paying everything you are owed?You have rights!Get a FREE claim review!CALL NOW!972-954-6845ADJUSTER FOR THE INSUREDI would like to see a photo in the back ground of a damaged home. I would like a design on both sides of the post card.Colors I prefer are navy as a base color and white text ( or red text for the CALL NOW and the phone number.I would like the message to communicate I am a licensed public adjuster working for the insured and I can help them get what they are owed from the insurance company.

```html
<!DOCTYPE html>
<html lang="en">
<head>
<meta charset="utf-8">
<title>Northgate Adjusters – Postcard Mailer</title>
<link href="https://fonts.googleapis.com/css2?family=Comic+Neue:ital,wght@0,400;0,700;1,700&family=Roboto+Condensed:wght@700&display=swap" rel="stylesheet">
<style>
  :root {
    --stage: #1c1c1c;
    --navy: #004b93;
    --navy-deep: #003a78;
    --blue: #0b6fc7;
    --sky: #4fb6e6;
    --steel: #4a8fd0;
    --text-navy: #1b3f8b;
    --red: #e0001b;
    --white: #ffffff;
    --paper-grey: #e6e8ec;
    --line-grey: #8a8a8a;
  }
  * { box-sizing: border-box; margin: 0; padding: 0; }
  html, body { width: 1200px; height: 1173px; overflow: hidden; }
  body { background: var(--stage); position: relative; font-family: "Comic Neue", sans-serif; }

  .card { position: absolute; overflow: hidden; background: var(--white); box-shadow: 0 10px 24px rgba(0,0,0,.6); }
  .card--front { left: 267px; top: 38px; width: 641px; height: 494px; }
  .card--back { left: 267px; top: 561px; width: 643px; height: 493px; }
  .card svg.art { position: absolute; inset: 0; }

  .brand { font-family: "Comic Neue", sans-serif; font-weight: 700; white-space: nowrap; }
  .front-copy { position: absolute; left: 6px; top: 128px; width: 298px; text-align: center; color: var(--text-navy); }
  .front-copy .brand { font-size: 30px; line-height: 1.1; }
  .front-copy .headline { font-size: 27px; font-weight: 700; line-height: 1.15; letter-spacing: 1px; margin-top: 2px; }
  .front-copy .tagline { font-family: "Roboto Condensed", sans-serif; font-size: 18.5px; font-weight: 700; margin-top: 3px; }
  .front-copy .pitch { font-size: 18px; line-height: 21px; margin-top: 8px; letter-spacing: .3px; }
  .front-copy .cta { font-size: 21px; font-weight: 700; line-height: 25px; margin-top: 8px; }

  .phone-pill { position: absolute; display: flex; align-items: center; justify-content: center; background: var(--red); border-radius: 50%; color: var(--white); font-family: "Roboto Condensed", sans-serif; font-weight: 700; }
  .card--front .phone-pill { left: 24px; top: 347px; width: 244px; height: 65px; font-size: 37px; }
  .card--back .phone-pill { left: 38px; top: 371px; width: 183px; height: 46px; font-size: 28px; }

  .back-brand { position: absolute; left: 24px; top: 22px; color: var(--white); font-size: 30px; line-height: 1; }
  .back-cta { position: absolute; left: 14px; top: 322px; width: 240px; text-align: center; color: var(--white); font-size: 18px; font-style: italic; font-weight: 700; line-height: 22px; text-shadow: 0 0 2px var(--red), 0 0 2px var(--red), 1px 1px 0 var(--red); }

  .stamp-box { position: absolute; left: 538px; top: 28px; width: 73px; height: 89px; border: 1px solid #b9b9b9; }
  .divider { position: absolute; left: 328px; top: 85px; width: 1px; height: 385px; background: #cfcfcf; }
  .address-line { position: absolute; left: 357px; width: 228px; height: 1px; background: var(--line-grey); }
</style>
</head>
<body>

<section class="card card--front">
  <svg class="art" width="641" height="494" viewBox="0 0 641 494">
    <defs>
      <radialGradient id="paper" cx="0.3" cy="0.5" r="0.7">
        <stop offset="0" stop-color="#ffffff"/><stop offset="1" stop-color="#d8dbe0"/>
      </radialGradient>
      <linearGradient id="stormPhoto" x1="0" y1="0" x2="0" y2="1">
        <stop offset="0" stop-color="#9fb9d6"/><stop offset=".45" stop-color="#6d6a5f"/><stop offset=".75" stop-color="#d9d3ad"/><stop offset="1" stop-color="#8a8a6c"/>
      </linearGradient>
    </defs>
    <rect width="641" height="494" fill="url(#paper)"/>
    <rect width="641" height="70" fill="var(--navy)"/>
    <path d="M0 48 Q320 30 641 60 L641 85 Q320 55 0 75 Z" fill="var(--blue)"/>
    <path d="M0 75 Q320 55 641 72 L641 90 Q360 70 0 110 Z" fill="var(--sky)"/>
    <path d="M0 110 Q360 70 641 90 L641 96 Q360 78 0 122 Z" fill="var(--navy)"/>
    <path d="M345 86 Q260 260 420 428 L641 428 L641 66 Z" fill="var(--sky)"/>
    <path d="M355 84 Q272 260 428 426 L641 426 L641 68 Z" fill="var(--white)"/>
    <path role="img" aria-label="Photo of a white house crushed by a fallen tree after a storm" d="M360 84 Q278 260 432 425 L641 425 L641 72 Z" fill="url(#stormPhoto)"/>
    <path d="M0 395 Q300 445 641 395 L641 494 L0 494 Z" fill="var(--paper-grey)"/>
    <path d="M0 403 Q300 455 641 400 L641 430 Q320 470 0 430 Z" fill="var(--sky)"/>
    <path d="M0 418 Q320 470 641 420 L641 452 Q320 480 0 445 Z" fill="var(--navy)"/>
    <path d="M0 448 Q300 480 641 455 L641 470 Q320 494 0 462 Z" fill="var(--white)"/>
    <path d="M0 462 Q320 494 641 470 L641 494 L0 494 Z" fill="var(--steel)"/>
  </svg>

  <div class="front-copy">
    <p class="brand">Northgate Adjusters</p>
    <p class="headline">Insurance Claim?</p>
    <p class="tagline">ADJUSTER FOR THE INSURED</p>
    <p class="pitch">Is your insurance paying<br>everything you are owed?<br>You have rights!</p>
    <p class="cta">Get a FREE claim review!<br>CALL NOW!</p>
  </div>
  <div class="phone-pill">641-387-2290</div>
</section>

<section class="card card--back">
  <svg class="art" width="643" height="493" viewBox="0 0 643 493">
    <defs>
      <linearGradient id="debrisPhoto" x1="0" y1="0" x2="0" y2="1">
        <stop offset="0" stop-color="#c7d6e6"/><stop offset=".25" stop-color="#cfc8a0"/><stop offset=".55" stop-color="#6b5a48"/><stop offset="1" stop-color="#8c7b60"/>
      </linearGradient>
    </defs>
    <rect x="0" y="0" width="322" height="493" fill="var(--white)"/>
    <rect width="322" height="75" fill="var(--navy)"/>
    <path d="M0 55 Q160 60 322 50 L322 70 Q160 78 0 72 Z" fill="var(--blue)"/>
    <path d="M0 72 Q160 78 322 62 L322 82 Q160 96 0 104 Z" fill="var(--sky)"/>
    <path d="M0 104 Q160 96 322 82 L322 90 Q160 100 0 110 Z" fill="var(--navy)"/>
    <path d="M240 95 Q330 250 230 430 L322 430 L322 90 Z" fill="var(--navy-deep)"/>
    <path d="M0 110 L248 100 Q322 260 232 428 L0 428 Z" fill="var(--white)"/>
    <path role="img" aria-label="Photo of a house reduced to debris after a tornado" d="M0 120 L250 108 Q310 260 222 428 L0 428 Z" fill="url(#debrisPhoto)"/>
    <path d="M0 405 Q160 440 322 420 L322 493 L0 493 Z" fill="var(--paper-grey)"/>
    <path d="M0 410 Q160 450 322 425 L322 445 Q160 470 0 430 Z" fill="var(--sky)"/>
    <path d="M0 430 Q160 470 322 445 L322 465 Q160 480 0 448 Z" fill="var(--navy)"/>
    <path d="M0 452 Q160 484 322 470 L322 493 L0 493 Z" fill="var(--steel)"/>
  </svg>

  <p class="brand back-brand">Northgate Adjusters</p>
  <p class="back-cta">Get a FREE claim review!<br>CALL NOW!</p>
  <div class="phone-pill">641-387-2290</div>

  <div class="divider"></div>
  <div class="stamp-box"></div>
  <div class="address-line" style="top:298px"></div>
  <div class="address-line" style="top:346px"></div>
  <div class="address-line" style="top:394px"></div>
</section>

</body>
</html>
```